" A clínica é familiar, formado por um Cirurgião plástico, médico vascular e fisioterapeuta dermatofuncional (estética). Porém ainda temos projeto de incluir outros profissionais da área da saúde. "

```html
<!DOCTYPE html>
<html lang="pt-BR">
<head>
<meta charset="UTF-8">
<title>Lumivale Clinic – Envelopes</title>
<link rel="stylesheet" href="https://fonts.googleapis.com/css2?family=Poppins:wght@400;500&display=swap">
<style>
  :root {
    --bg: #ecedeb;
    --paper: #ffffff;
    --teal: #2cb596;
    --teal-light: #5fd4b6;
    --teal-deep: #1f8f78;
    --slate: #263b44;
    --slate-dark: #1d2e35;
    --ink-soft: #d8dfe1;
    --shade: #eef1f1;
  }
  * { margin: 0; padding: 0; box-sizing: border-box; }
  html, body { width: 1200px; height: 1200px; overflow: hidden; }
  body {
    background: var(--bg);
    font-family: "Poppins", sans-serif;
    position: relative;
  }
  .envelope {
    position: absolute;
    left: 100px;
    width: 1000px;
    height: 440px;
    overflow: hidden;
    box-shadow: 0 10px 28px rgba(0,0,0,0.12);
  }
  .envelope--front { top: 110px; background: var(--paper); }
  .envelope--back { top: 640px; background: var(--slate); }
  .envelope__shapes { position: absolute; inset: 0; }

  .brand {
    position: absolute;
    display: flex;
    align-items: center;
    gap: 14px;
  }
  .brand__dot {
    width: 30px; height: 30px;
    border-radius: 50%;
    background: var(--teal);
  }
  .brand__text { display: flex; flex-direction: column; line-height: 1; }
  .brand__name { font-size: 38px; font-weight: 500; }
  .brand__sub {
    font-size: 12px; font-weight: 500;
    letter-spacing: 9px; margin-top: 6px; margin-left: 86px;
  }
  .envelope--front .brand { left: 70px; top: 80px; }
  .envelope--front .brand__name,
  .envelope--front .brand__sub { color: var(--slate); }
  .envelope--back .brand { left: 70px; top: 300px; }
  .envelope--back .brand__name,
  .envelope--back .brand__sub { color: var(--paper); }

  .watermark-area {
    position: absolute;
    right: 70px; top: 190px;
    width: 190px; height: 190px;
    border-radius: 50%;
    background: radial-gradient(circle, var(--shade) 0%, rgba(238,241,241,0) 70%);
  }

  .contact {
    position: absolute;
    right: 90px; top: 282px;
    list-style: none;
    color: var(--ink-soft);
    font-size: 14px;
    line-height: 1.6;
    font-weight: 400;
  }
</style>
</head>
<body>

  <section class="envelope envelope--front" aria-label="Envelope frente">
    <svg class="envelope__shapes" width="1000" height="440" viewBox="0 0 1000 440" aria-hidden="true">
      <polygon points="0,0 1000,0 1000,10 960,44 40,44 0,10" fill="var(--teal)"/>
      <polygon points="40,44 960,44 955,50 45,50" fill="var(--teal-light)"/>
      <rect x="0" y="412" width="1000" height="28" fill="var(--teal)"/>
      <polygon points="0,406 1000,406 1000,412 0,412" fill="var(--teal-light)"/>
    </svg>
    <div class="brand">
      <span class="brand__dot"></span>
      <span class="brand__text">
        <span class="brand__name">Lumivale</span>
        <span class="brand__sub">CLINIC</span>
      </span>
    </div>
    <div class="watermark-area" role="img" aria-label="Área decorativa clara da marca"></div>
  </section>

  <section class="envelope envelope--back" aria-label="Envelope verso">
    <svg class="envelope__shapes" width="1000" height="440" viewBox="0 0 1000 440" aria-hidden="true">
      <polygon points="0,0 1000,0 1000,40 0,40" fill="var(--teal)"/>
      <polygon points="0,40 1000,40 1000,52 0,52" fill="var(--teal-deep)"/>
      <polygon points="560,52 1000,52 1000,130" fill="var(--teal-light)" opacity="0.9"/>
      <polygon points="0,52 1000,52 1000,58 0,58" fill="var(--slate-dark)"/>
    </svg>
    <div class="brand">
      <span class="brand__dot"></span>
      <span class="brand__text">
        <span class="brand__name">Lumivale</span>
        <span class="brand__sub">CLINIC</span>
      </span>
    </div>
    <ul class="contact">
      <li>Phone: 11 4000-1234</li>
      <li>Address: Rua das Acácias, 240</li>
      <li>Cep 04500-000 - Cidade Nova - SP</li>
      <li>Website: www.lumivale.com.br</li>
    </ul>
  </section>

</body>
</html>
```